National Virtual accounting firm needs website designed

I need a wordpress website design for a national virtual accounting firm. I will upload my business card, logo, and postcards that I have had designed and followed the same style. I want a similar style to be followed so I can keep the running theme similar.

Services include:

Tax Services:
Tax preparation and planning services for Individuals, businesses, estates, and nonprofits
Full Service Payroll for Businesses
QVT Audit Representation

Consulting:
Entity Selection & Restructuring
Financial Projections & Forecasts
Retirement Planning
IPO Readiness

Accounting:
Bookkeeping
Reviews and Compilations
Payroll Services

Other Services:
CFO Services
Compliance Services
Controller Services
Software Implementations for Tenvolk, Brombalt, and Plovena.

Target Market(s)

small to medium size businesses, and individuals

Industry/Entity Type

accounting firms

Font styles to use
Sans Serif

Colors
59FF00
82FF00
B8FF75
E3FFCB
F4FFEA

Requirements
Must have
• Color schematics from the logo and post cards/business cards

```html
<!DOCTYPE html>
<html lang="en">
<head>
<meta charset="utf-8">
<title>Verdano – Business Advisors &amp; Consultants</title>
<link rel="stylesheet" href="https://fonts.googleapis.com/css2?family=Noto+Serif:wght@400;700&family=Poppins:wght@400;500;600&display=swap">
<style>
:root{
  --green:#4cb848;
  --lime:#8dc63f;
  --yellow:#ffcc00;
  --mint:#effdea;
  --pale:#f4ffea;
  --ink:#111;
  --grey:#444;
  --serif:'Noto Serif', Georgia, serif;
  --sans:'Poppins', Arial, sans-serif;
}
*{box-sizing:border-box;margin:0;padding:0}
html,body{width:1200px;height:2850px;overflow:hidden;background:#fff}
body{position:relative;font-family:var(--sans);color:var(--ink)}
.abs{position:absolute}
.layer{position:absolute;left:0;top:0}

/* header */
.brand{position:absolute;display:flex;align-items:center;gap:12px;font-family:var(--serif);font-weight:700;color:var(--ink)}
.brand-dot{width:26px;height:26px;border-radius:50%;background:var(--yellow)}
.site-brand{left:90px;top:34px;font-size:38px}
.nav{position:absolute;left:561px;top:40px;display:flex;gap:37px;font-family:var(--serif);font-size:15px}
.nav a{color:#fff;text-decoration:none}
.nav a.active{color:var(--yellow);text-decoration:underline}
.call-btn{position:absolute;left:980px;top:33px;width:132px;height:35px;background:var(--yellow);border-radius:3px;display:flex;align-items:center;justify-content:center;gap:9px;font-family:var(--serif);font-weight:700;font-size:16px;color:#111}

/* hero */
.hero-kicker{left:88px;top:168px;font-family:var(--serif);font-weight:700;font-size:34px;color:var(--green)}
.hero-title{left:88px;top:206px;font-family:var(--serif);font-weight:700;font-size:56px;line-height:56px;color:var(--ink)}
.hero-sub{left:94px;top:336px;font-family:var(--serif);font-size:20px;line-height:26px;color:var(--ink)}
.hero-sub b{color:var(--green)}
.btn{position:absolute;display:flex;align-items:center;justify-content:center;font-family:var(--serif);font-weight:700;border-radius:2px}
.btn-consult{left:93px;top:415px;width:259px;height:38px;background:var(--green);color:#fff;font-size:16px}

/* headings */
.section-title{position:absolute;left:0;width:1200px;text-align:center;font-family:var(--serif);font-weight:700;font-size:31px;letter-spacing:.5px}
.swoosh{position:absolute}

/* service cards */
.card{position:absolute;top:815px;width:238px;height:253px;background:#fff;box-shadow:0 2px 10px rgba(0,0,0,.08);border-bottom:2px solid var(--green);padding:34px 15px 0}
.card .icon{width:70px;height:50px;position:relative;margin-bottom:26px}
.card h3{font-family:var(--serif);font-size:17px;font-weight:700;color:var(--green);margin-bottom:10px}
.card ul{list-style:none;font-size:12.5px;line-height:17.5px;color:var(--grey);height:90px}
.card .more{font-family:var(--serif);font-weight:700;font-size:11px;color:var(--green);letter-spacing:.3px}
.card.featured{background:var(--green);border-bottom-color:var(--green)}
.card.featured h3,.card.featured ul,.card.featured .more{color:#fff}
.card.featured .more{text-decoration:underline}

/* about */
.about-title{left:618px;top:1322px;font-family:var(--serif);font-weight:700;font-size:31px;color:var(--ink)}
.about-lead{left:618px;top:1404px;width:440px;font-weight:600;font-size:15.5px;line-height:21px}
.about-text{left:618px;width:450px;font-size:14.5px;line-height:21px;color:#1a1a1a}
.btn-read{left:618px;top:1636px;width:145px;height:39px;background:var(--yellow);color:#111;font-size:16px}

/* inquiry */
.field{position:absolute;border:1px solid var(--lime);border-radius:4px;background:#fff;display:flex;align-items:flex-start;gap:9px;padding:11px 14px;font-size:13px;color:#777}
.btn-submit{left:541px;top:2150px;width:118px;height:38px;background:var(--lime);color:#fff;font-size:16px}

/* features */
.feature{position:absolute;top:2265px;display:flex;align-items:center;gap:14px;font-family:var(--serif);font-size:22px;color:var(--ink)}
.feature-badge{width:90px;height:90px;border-radius:50%;background:radial-gradient(circle at 40% 45%,var(--lime),var(--green));box-shadow:4px 0 0 var(--yellow);display:flex;align-items:center;justify-content:center}

/* footer */
.footer-brand{left:90px;top:2560px;font-size:35px}
.footer-head{position:absolute;top:2560px;font-family:var(--serif);font-weight:700;font-size:17px;color:var(--lime)}
.contact-list{left:393px;top:2600px;list-style:none;font-size:15px;line-height:20px;color:#111}
.contact-list li{display:flex;gap:12px;margin-bottom:14px}
.contact-list svg{flex:none;margin-top:3px}
.link-list{left:672px;top:2600px;list-style:none;font-size:15px;line-height:33px}
.link-list .active{color:var(--yellow);text-decoration:underline}
.map{left:850px;top:2490px;width:260px;height:260px;border-radius:50%;background:linear-gradient(135deg,#cfe3f5,#e9efe6 55%,#f2eee2);border:6px solid var(--yellow);box-shadow:inset 0 0 0 2px var(--lime)}
.bottom-bar{left:0;top:2812px;width:1200px;height:38px;background:var(--lime);display:flex;align-items:center;padding:0 88px;color:#fff;font-family:var(--serif);font-size:15px}
.socials{margin-left:auto;display:flex;gap:10px}
.socials span{width:24px;height:24px;border-radius:50%;border:1.5px solid #fff}
.socials span.active{background:var(--yellow);border-color:var(--yellow)}
</style>
</head>
<body>

<!-- hero background -->
<svg class="layer" width="1200" height="650" viewBox="0 0 1200 650" aria-hidden="true">
  <defs>
    <linearGradient id="photoTone" x1="0" y1="0" x2="1" y2="1">
      <stop offset="0" stop-color="#3a4048"/>
      <stop offset=".5" stop-color="#c9c4c2"/>
      <stop offset="1" stop-color="#e9dcd8"/>
    </linearGradient>
    <linearGradient id="heroBg" x1="0" y1="0" x2="0" y2="1">
      <stop offset="0" stop-color="#f1fdee"/>
      <stop offset="1" stop-color="#e6fbdc"/>
    </linearGradient>
  </defs>
  <rect width="1200" height="640" fill="url(#heroBg)"/>
  <path d="M525,0 C455,160 440,430 630,622 L1200,545 L1200,0 Z" fill="#f9cf2a"/>
  <path d="M0,480 C220,570 470,640 720,636 C920,632 1100,585 1200,538 L1200,560 C1080,610 920,650 720,650 C460,650 220,615 0,575 Z" fill="var(--lime)"/>
  <path d="M0,480 C200,540 330,570 470,590 C300,590 140,580 0,570 Z" fill="var(--green)"/>
</svg>
<svg class="layer" width="1200" height="650" viewBox="0 0 1200 650" role="img" aria-label="Photo of two women working at an office desk with laptops and coffee">
  <path d="M545,0 C478,160 462,430 650,618 C850,630 1050,590 1200,540 L1200,0 Z" fill="url(#photoTone)"/>
</svg>

<div class="brand site-brand"><span class="brand-dot"></span>Verdano</div>
<nav class="nav">
  <a class="active">HOME</a><a>ABOUT US</a><a>SERVICES</a><a>CONTACT US</a>
</nav>
<div class="call-btn">
  <svg width="14" height="14" viewBox="0 0 24 24"><path d="M6.6 10.8a15 15 0 0 0 6.6 6.6l2.2-2.2a1 1 0 0 1 1-.25 11 11 0 0 0 3.6.6 1 1 0 0 1 1 1V20a1 1 0 0 1-1 1A17 17 0 0 1 3 4a1 1 0 0 1 1-1h3.5a1 1 0 0 1 1 1c0 1.25.2 2.45.6 3.6a1 1 0 0 1-.25 1z" fill="#111"/></svg>
  Call Now!
</div>

<div class="abs hero-kicker">Business</div>
<h1 class="abs hero-title">Advisors &amp;<br>Consultants</h1>
<p class="abs hero-sub">Why Settle for Less When Your<br>Finances Could be <b>Verdano</b>?</p>
<div class="btn btn-consult">Shedule A Free Consult Now</div>

<!-- services -->
<h2 class="section-title" style="top:722px">SERVICES</h2>
<svg class="swoosh" style="left:530px;top:758px" width="140" height="16" viewBox="0 0 140 16"><path d="M2,12 Q60,-4 138,14 Q70,4 2,12Z" fill="var(--green)"/></svg>

<div class="card" style="left:88px">
  <div class="icon"><span class="abs" style="left:30px;top:6px;width:40px;height:40px;border-radius:50%;background:#d8f8cf"></span>
    <svg class="abs" width="50" height="50" viewBox="0 0 50 50" fill="none" stroke="var(--green)" stroke-width="2"><rect x="3" y="2" width="22" height="30"/><rect x="12" y="10" width="24" height="36"/><circle cx="20" cy="36" r="6"/><path d="M26 20h8M26 26h8"/></svg></div>
  <h3>Accounting</h3>
  <ul><li>Bookkeeping</li><li>Compilations &amp; Reviews</li><li>Payroll Services</li></ul>
  <div class="more">READ MORE</div>
</div>
<div class="card" style="left:350px">
  <div class="icon"><span class="abs" style="left:30px;top:6px;width:40px;height:40px;border-radius:50%;background:#d8f8cf"></span>
    <svg class="abs" width="50" height="50" viewBox="0 0 50 50" fill="none" stroke="var(--green)" stroke-width="2"><rect x="2" y="2" width="32" height="44"/><path d="M8 10h16M8 22h14M8 28h14M8 34h14"/><rect x="24" y="24" width="18" height="22"/></svg></div>
  <h3>Tax</h3>
  <ul><li>Individual Tax Preparation</li><li>Business Tax Preparation</li><li>Estate &amp; Trust Preparation</li><li>Audit Representation</li></ul>
  <div class="more">READ MORE</div>
</div>
<div class="card featured" style="left:612px">
  <div class="icon"><span class="abs" style="left:30px;top:6px;width:40px;height:40px;border-radius:50%;background:var(--yellow)"></span>
    <svg class="abs" width="50" height="50" viewBox="0 0 50 50" fill="none" stroke="#fff" stroke-width="2"><circle cx="10" cy="10" r="5"/><circle cx="34" cy="14" r="5"/><path d="M4 46V24h12v22M28 46V28h12v18M18 4h16v6"/></svg></div>
  <h3>Consulting</h3>
  <ul><li>Entity Selection &amp; Restructuring</li><li>Financial Projections &amp; Forcasts</li><li>Retirement Planning</li><li>IPO Readiness</li></ul>
  <div class="more">READ MORE</div>
</div>
<div class="card" style="left:874px">
  <div class="icon"><span class="abs" style="left:30px;top:6px;width:40px;height:40px;border-radius:50%;background:#d8f8cf"></span>
    <svg class="abs" width="50" height="50" viewBox="0 0 50 50" fill="none" stroke="var(--green)" stroke-width="2"><rect x="2" y="4" width="32" height="42"/><path d="M12 2h12v6H12zM8 16h4M16 16h12M8 26h4M16 26h12M8 36h4"/><circle cx="38" cy="40" r="7"/><path d="M35 40l2 2 4-4"/></svg></div>
  <h3>Additional Services</h3>
  <ul><li>CFO Services</li><li>Compliance Services</li><li>Controller Services</li><li>Software Implementations</li></ul>
  <div class="more">READ MORE</div>
</div>

<!-- about band -->
<svg class="layer" style="top:1190px" width="1200" height="670" viewBox="0 0 1200 670" aria-hidden="true">
  <path d="M0,70 Q600,-20 1200,30 L1200,560 Q700,590 0,590 Z" fill="var(--green)"/>
  <path d="M0,82 Q600,10 1200,58 L1200,545 Q700,580 0,580 Z" fill="var(--lime)"/>
  <circle cx="245" cy="355" r="313" fill="#f9cf2a"/>
</svg>
<svg class="layer" style="top:1190px" width="1200" height="670" viewBox="0 0 1200 670" role="img" aria-label="Photo of two businessmen shaking hands in an office">
  <defs><linearGradient id="aboutTone" x1="0" y1="0" x2="1" y2="1"><stop offset="0" stop-color="#6d7f92"/><stop offset=".55" stop-color="#c7d3df"/><stop offset="1" stop-color="#8fa6c2"/></linearGradient></defs>
  <circle cx="228" cy="355" r="305" fill="url(#aboutTone)"/>
</svg>

<h2 class="abs about-title">ABOUT US</h2>
<svg class="swoosh" style="left:626px;top:1360px" width="120" height="14" viewBox="0 0 140 16"><path d="M2,12 Q60,-4 138,14 Q70,4 2,12Z" fill="var(--green)"/></svg>
<p class="abs about-lead">Lorem Ipsum is simply dummy text of the printing and typesetting industry.</p>
<p class="abs about-text" style="top:1467px">Lorem Ipsum has been the industry's standard dummy text ever since the 1500s, when an unknown printer took a galley of type and scrambled it to make a type specimen book.</p>
<p class="abs about-text" style="top:1551px">It has survived not only five centuries, but also the leap into electronic typesetting, remaining essentially unchanged.</p>
<div class="btn btn-read">Read More</div>

<!-- quick inquiry -->
<h2 class="section-title" style="top:1878px">QUICK INQUIRY</h2>
<svg class="swoosh" style="left:530px;top:1914px" width="140" height="16" viewBox="0 0 140 16"><path d="M2,12 Q60,-4 138,14 Q70,4 2,12Z" fill="var(--green)"/></svg>

<div class="field" style="left:300px;top:1972px;width:292px;height:38px"><svg width="14" height="14" viewBox="0 0 24 24" fill="none" stroke="var(--green)" stroke-width="2"><circle cx="12" cy="8" r="4"/><path d="M4 22c0-5 4-7 8-7s8 2 8 7"/></svg>Name</div>
<div class="field" style="left:300px;top:2022px;width:292px;height:38px"><svg width="14" height="14" viewBox="0 0 24 24" fill="none" stroke="var(--green)" stroke-width="2"><rect x="2" y="5" width="20" height="14"/><path d="M2 5l10 8 10-8"/></svg>Email</div>
<div class="field" style="left:300px;top:2072px;width:292px;height:38px"><svg width="14" height="14" viewBox="0 0 24 24" fill="none" stroke="var(--green)" stroke-width="2"><rect x="7" y="2" width="10" height="20" rx="2"/></svg>Phone</div>
<div class="field" style="left:608px;top:1972px;width:292px;height:138px"><svg width="14" height="14" viewBox="0 0 24 24" fill="none" stroke="var(--green)" stroke-width="2"><path d="M3 3h18v12l-6 6H3z"/></svg>Message</div>
<div class="btn btn-submit">Submit</div>

<!-- features -->
<div class="feature" style="left:152px"><span class="feature-badge"><svg width="44" height="44" viewBox="0 0 44 44" fill="none" stroke="#fff" stroke-width="2"><circle cx="16" cy="16" r="9"/><circle cx="30" cy="30" r="9"/><path d="M30 25v5l3 3"/></svg></span>EXPIRIENCED</div>
<div class="feature" style="left:472px"><span class="feature-badge"><svg width="44" height="44" viewBox="0 0 44 44" fill="none" stroke="#fff" stroke-width="2"><circle cx="14" cy="12" r="4"/><circle cx="30" cy="12" r="4"/><path d="M6 26c0-5 16-5 16 0M22 26c0-5 16-5 16 0M4 32h36v8H4z"/></svg></span>PROFESSIONAL</div>
<div class="feature" style="left:809px"><span class="feature-badge"><svg width="44" height="44" viewBox="0 0 44 44" fill="none" stroke="#fff" stroke-width="2"><circle cx="24" cy="14" r="9"/><path d="M24 9v10M4 30h10l8 4h14l4-5M4 40h30"/></svg></span>AFFORDABLE</div>

<!-- footer -->
<svg class="layer" style="top:2420px" width="1200" height="400" viewBox="0 0 1200 400" aria-hidden="true">
  <path d="M0,120 Q500,-20 1200,80 L1200,400 L0,400 Z" fill="var(--pale)"/>
  <path d="M0,120 Q480,-30 1200,70 L1200,100 Q480,10 0,135 Z" fill="var(--lime)"/>
  <path d="M700,20 Q1000,30 1200,90 L1200,150 Q1000,60 700,20 Z" fill="var(--green)"/>
</svg>

<div class="brand footer-brand"><span class="brand-dot"></span>Verdano</div>

<div class="footer-head" style="left:393px">CONATCT INFO</div>
<ul class="abs contact-list">
  <li><svg width="14" height="16" viewBox="0 0 24 24"><path d="M12 2a7 7 0 0 0-7 7c0 5 7 13 7 13s7-8 7-13a7 7 0 0 0-7-7zm0 9.5A2.5 2.5 0 1 1 12 6.5a2.5 2.5 0 0 1 0 5z" fill="var(--yellow)"/></svg><span>Lorem ipsum Maple<br>ln., Fairview, CA 90000</span></li>
  <li><svg width="14" height="14" viewBox="0 0 24 24"><path d="M6.6 10.8a15 15 0 0 0 6.6 6.6l2.2-2.2a1 1 0 0 1 1-.25 11 11 0 0 0 3.6.6 1 1 0 0 1 1 1V20a1 1 0 0 1-1 1A17 17 0 0 1 3 4a1 1 0 0 1 1-1h3.5a1 1 0 0 1 1 1c0 1.25.2 2.45.6 3.6a1 1 0 0 1-.25 1z" fill="var(--yellow)"/></svg><span>(555) 014-2287</span></li>
  <li><svg width="14" height="14" viewBox="0 0 24 24"><rect x="3" y="8" width="18" height="13" fill="var(--yellow)"/><rect x="7" y="3" width="10" height="6" fill="var(--yellow)"/></svg><span>(555) 014-9930</span></li>
  <li><svg width="14" height="14" viewBox="0 0 24 24"><rect x="2" y="5" width="20" height="14" fill="var(--yellow)"/><path d="M2 5l10 8 10-8" stroke="#fff" stroke-width="2" fill="none"/></svg><span>office@verdano.com</span></li>
</ul>

<div class="footer-head" style="left:669px">QUICK LINKS</div>
<ul class="abs link-list">
  <li class="active">Home</li><li>About Us</li><li>Services</li><li>Contact Us</li>
</ul>

<div class="abs map" role="img" aria-label="Street map showing the office location"></div>

<div class="abs bottom-bar">
  © 2023 Verdano. All Right Reserved
  <div class="socials"><span></span><span class="active"></span><span></span><span></span></div>
</div>

</body>
</html>
```